Quorvant Group Invitation

I need an invitation designed for both online and hard copy distribution. I'm uploading a poorly designed online invitation that includes our logo and the blue and black colors we want to use. The online invitation must have an area to embed video (see attached).

With regard to the hard copy invitation, we need it to be a 5x7 card. Where the embedded video is on the online version, we would like you to create an image that represents the terms "monetizing innovation". If you go to www.qvgroup.co, you can see what the company is using to express those words right now. There are no limitations to what you come up with for this visual.

Please note: The invitation both online and hardcopy must be designed so that all the information in the attached copy can be read. This includes: Logo, hosted by; When/date, where, two quotes, etc.

I've attached our logo files. You can use whichever logo file you want for your design.

Many thanks...looking forward to seeing all your great designs.
Updates

All - you do not need to follow our format for the invite as long as all the information we need is on it....Note:  we will need to be able to edit the information for other presentation.

EPS files of the logo have been added for those of you who have requested it.

Many thanks,

Marla

Reason: All, Apologies for the extension. The decision-makers have been travelling and have not had a chance to thoroughly review the designs. We really appreciate your patience. Many thanks, Marla

Target Market(s)

Investors and Media

Industry/Entity Type

It Company

Requirements
Must have
• Please use the blue and black colors as seen in the attached uploaded files.

```html
<!DOCTYPE html>
<html lang="en">
<head>
<meta charset="utf-8">
<title>Quorvant Group – Investor Presentation Invitation</title>
<link rel="stylesheet" href="https://fonts.googleapis.com/css2?family=Alegreya+Sans+SC:wght@500;700;800&display=swap">
<style>
  :root {
    --ink: #000000;
    --paper: #ffffff;
    --accent-blue: #86aee0;
    --quote-grey: #a3a3a3;
    --rsvp-grey: #5a5a5a;
    --band-grey: #d7d7d7;
    --frame: #333333;
    --source-navy: #1f2f5c;
  }
  * { margin: 0; padding: 0; box-sizing: border-box; }
  html, body { width: 1200px; height: 900px; overflow: hidden; background: var(--paper); }
  body { font-family: "Alegreya Sans SC", sans-serif; position: relative; }
  .abs { position: absolute; white-space: nowrap; }
  .invite-frame { position: absolute; left: 66px; top: 37px; width: 1068px; height: 824px; border: 1px solid var(--frame); }
  .header-panel { position: absolute; left: 97px; top: 37px; }

  .label { color: var(--accent-blue); font-weight: 800; font-size: 17px; letter-spacing: 1.6px; line-height: 20px; }
  .detail { color: var(--paper); font-size: 16.5px; line-height: 20.5px; letter-spacing: 1.5px; font-weight: 700; }
  .divider { left: 133px; top: 284px; width: 148px; border-top: 2px dotted var(--paper); }
  .site { left: 133px; top: 296px; color: var(--paper); font-size: 16px; font-weight: 800; letter-spacing: 1.6px; }

  .presenting-band { left: 718px; top: 72px; width: 380px; height: 26px; background: var(--band-grey); border-radius: 6px 0 0 6px; font-size: 17px; font-weight: 800; letter-spacing: 2.6px; padding: 2px 0 0 14px; color: var(--ink); }
  .brand-name { left: 840px; top: 143px; color: var(--paper); font-size: 26px; line-height: 26px; letter-spacing: 5px; font-weight: 700; }

  .quote { color: var(--quote-grey); font-size: 20.5px; line-height: 28px; letter-spacing: 2.3px; font-weight: 700; }
  .quote-mark { color: var(--quote-grey); font-size: 46px; font-weight: 800; line-height: 1; }
  .quote-close { display: inline-block; color: var(--quote-grey); font-size: 46px; font-weight: 800; line-height: 0; vertical-align: -14px; margin-left: 6px; }
  .source { font-size: 26px; font-weight: 800; letter-spacing: 0.6px; }
  .source-navy { color: var(--source-navy); }
  .source-dark { color: var(--ink); }

  .video-frame { left: 618px; top: 340px; width: 446px; height: 289px; border: 2px solid #9a9a9a; border-radius: 10px; overflow: hidden; background: #f1f1f1; }
  .video-still { position: absolute; inset: 0 0 20px 0; background: linear-gradient(135deg, #ffffff 0%, #d9d9d9 45%, #3a3a3a 75%, #ffffff 100%); }
  .player-bar { position: absolute; left: 0; right: 0; bottom: 0; height: 20px; background: linear-gradient(#d8dde4, #9aa4b0); }

  .rsvp { left: 634px; top: 652px; color: var(--rsvp-grey); font-size: 16px; font-weight: 800; letter-spacing: 1.6px; line-height: 22px; }
  .rsvp strong { color: var(--ink); }
  .notice-panel { left: 593px; top: 753px; width: 505px; height: 108px; background: var(--ink); border-radius: 16px 16px 0 0; }
  .notice { left: 622px; top: 777px; color: var(--paper); font-size: 14.5px; font-weight: 800; letter-spacing: 1.6px; line-height: 20px; }
</style>
</head>
<body>
  <div class="invite-frame"></div>

  <svg class="header-panel" width="1002" height="318" viewBox="0 0 1002 318" aria-hidden="true">
    <path d="M0 0 H1001 V228 Q1001 250 980 254 L22 316 Q0 318 0 296 Z" fill="#000"/>
  </svg>

  <div class="abs label" style="left:133px;top:80px;">Hosted By:</div>
  <div class="abs detail" style="left:133px;top:100px;">
    Rami Haddad, CEO<br>Dean Whitford, President<br>Luis Carrera, CFO<br>Scott Ambler, COO<br>Adam Kessler, CCO
  </div>

  <div class="abs label" style="left:393px;top:80px;">When:</div>
  <div class="abs detail" style="left:393px;top:100px;">
    Wednesday, September 28th<br>Check-In 3:00 pm<br>Presentation 3:30 - 4:30 pm
  </div>

  <div class="abs label" style="left:393px;top:184px;">Where:</div>
  <div class="abs detail" style="left:393px;top:205px;">
    Linden Inn – Garden Room<br>2418 Linden Ave<br>Ashford CA 90210
  </div>

  <div class="abs divider"></div>
  <div class="abs site">www.qvgroup.co</div>

  <div class="abs presenting-band">A SPECIAL PRESENTATION OF</div>
  <div class="abs brand-name">QUORVANT<br>GROUP</div>

  <div class="abs quote-mark" style="left:118px;top:390px;">“</div>
  <div class="abs quote" style="left:160px;top:394px;">
    In the biggest breakthrough<br>against malaria in years,<br>scientist yesterday said<br>they had identified the<br>odor molecules that baffle<br>blood-thirsty mosquitoes<span class="quote-close">”</span>
  </div>
  <div class="abs source source-navy" style="left:272px;top:584px;">The Southern Ledger</div>

  <div class="abs quote-mark" style="left:175px;top:664px;">“</div>
  <div class="abs quote" style="left:217px;top:668px;">
    Confusing mosquitoes to<br>fight deadly disease<span class="quote-close">”</span>
  </div>
  <div class="abs source source-dark" style="left:165px;top:744px;">Coastal Daily Times</div>

  <div class="abs video-frame">
    <div class="video-still" role="img" aria-label="Video still: honeycomb of white, grey and black hexagons with the words Monetizing Innovation"></div>
    <svg class="abs" style="left:190px;top:104px;" width="60" height="60" viewBox="0 0 60 60" aria-hidden="true">
      <circle cx="30" cy="30" r="27" fill="rgba(60,60,60,0.75)" stroke="#ddd" stroke-width="3"/>
      <path d="M23 17 L42 30 L23 43 Z" fill="#fff"/>
    </svg>
    <div class="player-bar">
      <svg width="442" height="20" viewBox="0 0 442 20" aria-hidden="true">
        <circle cx="11" cy="10" r="6" fill="#556"/>
        <path d="M9 7 L14 10 L9 13 Z" fill="#fff"/>
        <rect x="22" y="7" width="270" height="6" rx="3" fill="#5b7fa8"/>
        <circle cx="40" cy="10" r="4" fill="#fff"/>
        <rect x="296" y="4" width="72" height="12" rx="6" fill="#667"/>
        <text x="332" y="13.5" font-family="Arial, sans-serif" font-size="9" fill="#fff" text-anchor="middle">00:11 / 03:33</text>
        <rect x="384" y="7" width="40" height="6" rx="3" fill="#333"/>
        <circle cx="412" cy="10" r="3" fill="#fff"/>
      </svg>
    </div>
  </div>

  <div class="abs rsvp">
    Please <strong>RSVP</strong> by <strong>Monday, September 26th</strong><br>
    Joanna Reyes (877) 555-0142 x1003<br>
    jreyes@qvgroup.co
  </div>

  <div class="abs notice-panel"></div>
  <div class="abs notice">* Please note that you must be an accredited<br>&nbsp;&nbsp;investor to attend the presentation</div>
</body>
</html>
```